Stridewell Outfitters Stationary

At Stridewell Outfit, we know that rehab technology is much more than a tool or machine. It’s mobility for your body and productivity and freedom for your lifestyle to reclaim your life. That’s why we specialize in custom power and manual wheelchairs, scooters, complex seating and positioning, standers, and bathroom equipment that all help you reclaim your life.

Our rehab equipment includes custom power wheelchairs offering complex, customized seating and positioning systems with an array of specialized electronic control features. With a certified staff of Assistive Technology Professionals (ATPs) and technical repair department, we provide knowledgeable assistance to make sure you get the right products needed to reclaim your life – delivered on time, right to your door.

```html
<!DOCTYPE html>
<html lang="en">
<head>
<meta charset="utf-8">
<title>Stridewell Outfitters Stationery</title>
<link rel="stylesheet" href="https://fonts.googleapis.com/css2?family=Montserrat:wght@600&family=Arimo:wght@400;700&display=swap">
<style>
  :root {
    --navy: #0d3559;
    --green: #8dc63f;
    --paper: #ffffff;
    --backdrop: #ececec;
    --ink: #3a3a3a;
    --muted: #6b6b6b;
  }
  * { box-sizing: border-box; margin: 0; padding: 0; }
  html, body { width: 1200px; height: 937px; overflow: hidden; }
  body {
    background: var(--backdrop);
    font-family: "Arimo", Arial, sans-serif;
    color: var(--ink);
    position: relative;
  }
  .sheet {
    position: absolute;
    background: var(--paper);
    box-shadow: 0 2px 8px rgba(0,0,0,0.12);
    overflow: hidden;
  }
  .wave {
    position: absolute;
    left: 0; bottom: 0;
    width: 100%;
    display: block;
  }
  .brand {
    position: absolute;
    display: flex;
    align-items: center;
    gap: 0.35em;
    font-family: "Montserrat", Arial, sans-serif;
    font-weight: 600;
    color: var(--navy);
    line-height: 1.05;
  }
  .brand-dot {
    width: 0.9em; height: 0.9em;
    border-radius: 50%;
    background: var(--green);
    flex: none;
  }
  .brand-name { display: block; }

  /* Letterhead */
  .letterhead { left: 185px; top: 68px; width: 385px; height: 544px; }
  .letterhead .brand { left: 40px; top: 42px; font-size: 20px; }
  .contact-list {
    position: absolute; right: 18px; top: 22px;
    list-style: none; text-align: right;
    font-size: 4.6px; color: var(--muted); line-height: 8px;
  }
  .contact-list li::after {
    content: ""; display: inline-block;
    width: 5px; height: 5px; border-radius: 50%;
    background: var(--navy); margin-left: 3px; vertical-align: -1px;
  }
  .letter-body {
    position: absolute; left: 36px; top: 138px; width: 300px;
    font-size: 5.2px; line-height: 7.6px; color: var(--ink);
  }
  .letter-body p { margin-bottom: 7px; }
  .letter-body .gap { margin-bottom: 20px; }
  .signature {
    width: 32px; height: 16px; margin: 2px 0 6px;
    background: linear-gradient(90deg, #f2f2f2, #e6e6e6);
  }
  .signer { font-weight: 700; }

  /* Folder */
  .folder { left: 636px; top: 41px; width: 458px; height: 575px; }
  .folder .brand { left: 100px; top: 270px; font-size: 38px; }

  /* Business cards */
  .card { width: 177px; height: 98px; border-radius: 8px; }
  .card-front { left: 45px; top: 659px; }
  .card-front .brand { left: 48px; top: 14px; font-size: 9px; }
  .card-person {
    position: absolute; left: 12px; top: 38px; width: 74px;
    text-align: right; font-size: 4.2px; line-height: 5.6px; color: var(--muted);
  }
  .card-person .person-name { color: var(--navy); font-weight: 700; font-size: 5px; }
  .card-person .person-role { margin-bottom: 4px; }
  .card-contacts {
    position: absolute; left: 92px; top: 38px;
    border-left: 0.5px solid var(--muted); padding-left: 3px;
    list-style: none; font-size: 4.2px; line-height: 5.6px; color: var(--muted);
  }
  .card-back { left: 45px; top: 785px; }
  .card-back .brand-mark {
    position: absolute; left: 12px; top: 14px;
    width: 56px; height: 56px; border-radius: 50%;
    background: var(--green);
  }
  .card-back .brand { left: 86px; top: 60px; font-size: 9px; }

  /* Envelopes */
  .envelope-front { left: 265px; top: 672px; width: 432px; height: 207px; }
  .envelope-front .brand { left: 16px; top: 38px; font-size: 17px; }
  .envelope-back { left: 737px; top: 672px; width: 417px; height: 207px; }
  .envelope-flap {
    position: absolute; left: 0; top: 0; width: 100%; height: 72px;
    background: var(--navy);
    border-radius: 0 0 38px 38px;
    display: flex; align-items: center; justify-content: center;
  }
  .web-address {
    color: #ffffff; font-size: 12.5px; letter-spacing: 1.6px;
    font-family: "Arimo", Arial, sans-serif;
  }
</style>
</head>
<body>

<svg width="0" height="0" style="position:absolute" aria-hidden="true">
  <defs>
    <symbol id="footer-wave" viewBox="0 0 400 40" preserveAspectRatio="none">
      <path d="M0,16 C120,6 260,2 400,0 L400,9 C260,13 120,20 0,28 Z" fill="#8dc63f"/>
      <path d="M0,33 C140,22 270,15 400,13 L400,40 L0,40 Z" fill="#0d3559"/>
    </symbol>
  </defs>
</svg>

<!-- Letterhead -->
<section class="sheet letterhead">
  <div class="brand"><span class="brand-dot"></span><span class="brand-name">Stridewell<br>Outfitters</span></div>
  <ul class="contact-list">
    <li>012 345 6789</li>
    <li>012 345 6790</li>
    <li>hello@stridewelloutfit.com</li>
    <li>www.stridewelloutfit.com</li>
    <li>12 Harbor Lane, Millbrook 4410</li>
  </ul>
  <div class="letter-body">
    <p>July 2, 2012</p>
    <p><strong>Dear CH,</strong><br>12 Harbor Lane, Millbrook</p>
    <p class="gap">is simply dummy text of the printing and typesetting industry. Lorem Ipsum has been the industry's standard dummy text ever since the 1500s, when an unknown printer took a galley of type and scrambled it to make a type specimen book. It has survived not only five centuries, but also the leap into electronic typesetting, remaining essentially unchanged. It was popularised in the 1960s with the release of Letraset sheets containing Lorem Ipsum passages, and more recently with desktop publishing software including versions of Lorem Ipsum.</p>
    <p class="gap">is simply dummy text of the printing and typesetting industry. Lorem Ipsum has been the industry's standard dummy text ever since the 1500s, when an unknown printer took a galley of type and scrambled it to make</p>
    <p>is simply dummy text of the printing and typesetting industry. Lorem Ipsum has been the industry's standard dummy text ever since the 1500s, when an unknown printer took a galley of type and scrambled it to make a type specimen book. It has survived not only five centuries, but also the leap into electronic typesetting, remaining essentially unchanged. It was popularised in the 1960s with the release of Letraset sheets containing Lorem Ipsum passages, and more recently with desktop publishing software including versions of Lorem Ipsum.</p>
    <p>Best Regards,</p>
    <div class="signature" role="img" aria-label="Handwritten signature"></div>
    <p><span class="signer">Dana Whitfield</span><br>Director<br><br>12 Harbor Lane, Millbrook</p>
  </div>
  <svg class="wave" height="32"><use href="#footer-wave"/></svg>
</section>

<!-- Presentation folder -->
<section class="sheet folder">
  <div class="brand"><span class="brand-dot"></span><span class="brand-name">Stridewell<br>Outfitters</span></div>
  <svg class="wave" height="40"><use href="#footer-wave"/></svg>
</section>

<!-- Business card front -->
<section class="sheet card card-front">
  <div class="brand"><span class="brand-dot"></span><span class="brand-name">Stridewell<br>Outfitters</span></div>
  <div class="card-person">
    <div class="person-name">Ravi Holm</div>
    <div class="person-role">Owner / CEO</div>
    <div>Suite 8, 250 Oak Road,<br>Millbrook 4410</div>
  </div>
  <ul class="card-contacts">
    <li>+1 555 014 7890</li>
    <li>+1 555 014 7891</li>
    <li>555 014 1200</li>
    <li>ravi@stridewelloutfit.com</li>
    <li>www.stridewelloutfit.com</li>
  </ul>
  <svg class="wave" height="14"><use href="#footer-wave"/></svg>
</section>

<!-- Business card back -->
<section class="sheet card card-back">
  <div class="brand-mark"></div>
  <div class="brand"><span class="brand-name">Stridewell<br>Outfitters</span></div>
</section>

<!-- Envelope front -->
<section class="sheet envelope-front">
  <div class="brand"><span class="brand-dot"></span><span class="brand-name">Stridewell<br>Outfitters</span></div>
  <svg class="wave" height="44"><use href="#footer-wave"/></svg>
</section>

<!-- Envelope back -->
<section class="sheet envelope-back">
  <div class="envelope-flap"><span class="web-address">www.stridewelloutfit.com</span></div>
</section>

</body>
</html>
```